Real Estate Investment Company Needs A Business Card Designed

I need a business card designed for my use. We are a real estate investment company based in Omaha, Nebraska that specializes in buying, rehabbing and selling single family and multifamily properties. Would love designs that incorporate our logo and colors

Industry/Entity Type

Business

Contact Information for Business Card

Mitchell Parkhurst | President & CEO
4873 North 52nd Avenue, Ste 700
Omaha, NE 68142
(402) 786-4259
mitchell@kestrelgateproperties.example
www.KestrelgateProperties.example

Font styles to use
Serif

Colors
0255a3
3276b5

Requirements
Must have
• Our logo

```html
<!DOCTYPE html>
<html lang="en">
<head>
<meta charset="utf-8">
<title>Kestrelgate Properties – Business Card</title>
<link rel="stylesheet" href="https://fonts.googleapis.com/css2?family=Arimo:wght@400;700&display=swap">
<style>
  :root {
    --backdrop: #2b2b2d;
    --card: #1c1c1e;
    --card-edge: #262628;
    --brand-blue: #3276b5;
    --brand-blue-deep: #0255a3;
    --text-light: #c9c9cc;
    --silver: #b9b9bd;
  }
  * { box-sizing: border-box; margin: 0; padding: 0; }
  html, body {
    width: 1200px; height: 1189px; overflow: hidden;
    background: var(--backdrop);
    font-family: "Arimo", Arial, sans-serif;
  }
  .canvas { position: relative; width: 1200px; height: 1189px; }
  .card {
    position: absolute; left: 190px;
    width: 820px; height: 468px;
    background: var(--card);
    border: 1px solid var(--card-edge);
    border-radius: 36px;
    box-shadow: 0 18px 40px rgba(0,0,0,0.45);
  }
  .card--back { top: 70px; }
  .card--front { top: 640px; }

  .back-mark {
    position: absolute; left: 50%; top: 50%;
    transform: translate(-50%, -50%);
    display: flex; flex-direction: column; align-items: center; gap: 22px;
  }
  .back-mark__dot {
    width: 120px; height: 120px; border-radius: 50%;
    background: linear-gradient(160deg, #d4d4d8, #6e6e73);
  }
  .back-mark__name {
    color: var(--silver); font-weight: 700;
    font-size: 34px; letter-spacing: 1px; text-align: center; line-height: 1.15;
  }
  .back-mark__name span { display: block; font-size: 16px; letter-spacing: 5px; }

  .front-brand {
    position: absolute; left: 70px; top: 62px;
    color: var(--brand-blue); font-weight: 700; line-height: 1.1;
  }
  .front-brand__main { display: block; font-size: 40px; letter-spacing: 0.5px; }
  .front-brand__sub { display: block; font-size: 17px; letter-spacing: 6px; margin-left: 4px; }

  .person { position: absolute; left: 70px; top: 182px; }
  .person__name { color: var(--brand-blue); font-size: 27px; }
  .person__title { color: var(--text-light); font-size: 20px; margin-top: 2px; }

  .contacts { position: absolute; left: 70px; top: 262px; list-style: none; }
  .contacts li {
    display: flex; align-items: center; gap: 10px;
    color: var(--text-light); font-size: 20px; line-height: 30px;
  }
  .contacts svg { width: 20px; height: 20px; flex: none; }

  .address {
    position: absolute; left: 70px; top: 372px;
    color: var(--text-light); font-size: 22px; line-height: 30px; font-style: normal;
  }

  .front-disc {
    position: absolute; right: 70px; top: 84px;
    width: 300px; height: 300px; border-radius: 50%;
    background: linear-gradient(160deg, #5a9ad8, var(--brand-blue-deep));
  }
</style>
</head>
<body>
<main class="canvas">
  <section class="card card--back" aria-label="Card back">
    <div class="back-mark">
      <div class="back-mark__dot"></div>
      <div class="back-mark__name">KESTRELGATE<span>PROPERTIES</span></div>
    </div>
  </section>

  <section class="card card--front" aria-label="Card front">
    <div class="front-brand">
      <span class="front-brand__main">KESTRELGATE</span>
      <span class="front-brand__sub">PROPERTIES</span>
    </div>

    <div class="person">
      <p class="person__name">Mitchell Parkhurst</p>
      <p class="person__title">President &amp; CEO</p>
    </div>

    <ul class="contacts">
      <li>
        <svg viewBox="0 0 20 20" aria-hidden="true"><circle cx="10" cy="10" r="10" fill="#3276b5"/><path d="M6.5 5.5l2 .3.6 2.2-1.2.9a7 7 0 0 0 3.2 3.2l.9-1.2 2.2.6.3 2c-.6.8-1.6 1-2.6.7A9 9 0 0 1 6.2 8.1c-.3-1 0-2 .3-2.6z" fill="#1c1c1e"/></svg>
        (402) 786-4259
      </li>
      <li>
        <svg viewBox="0 0 20 20" aria-hidden="true"><circle cx="10" cy="10" r="10" fill="#3276b5"/><rect x="5" y="6.5" width="10" height="7" fill="none" stroke="#1c1c1e" stroke-width="1.4"/><path d="M5 6.5l5 4 5-4" fill="none" stroke="#1c1c1e" stroke-width="1.4"/></svg>
        mitchell@kestrelgateproperties.example
      </li>
      <li>
        <svg viewBox="0 0 20 20" aria-hidden="true"><circle cx="10" cy="10" r="10" fill="#3276b5"/><circle cx="10" cy="10" r="5.5" fill="none" stroke="#1c1c1e" stroke-width="1.2"/><ellipse cx="10" cy="10" rx="2.3" ry="5.5" fill="none" stroke="#1c1c1e" stroke-width="1.2"/><path d="M4.5 10h11" stroke="#1c1c1e" stroke-width="1.2"/></svg>
        www.KestrelgateProperties.example
      </li>
    </ul>

    <address class="address">4873 North 52nd Avenue, Ste 700<br>Omaha, NE 68142</address>

    <div class="front-disc"></div>
  </section>
</main>
</body>
</html>
```